Brindale transport business cards

Front of card, Looking for my logo on one side of the card

Back of card,
Brindale Transport Maintenance
Onsite Cars, Trucks & trailer maintenance and repairs
Ronan Brindale
0452819036
Brindaletm@fernmail.com

```html
<!DOCTYPE html>
<html lang="en">
<head>
<meta charset="utf-8">
<title>Brindale Transport Business Cards</title>
<link href="https://fonts.googleapis.com/css2?family=Montserrat:wght@400;600;800&family=Black+Ops+One&display=swap" rel="stylesheet">
<style>
  :root {
    --backdrop: #2e2e2e;
    --card: #ffffff;
    --ink: #111111;
    --brand-blue: #1f5fae;
    --text-muted: #333333;
  }
  * { margin: 0; padding: 0; box-sizing: border-box; }
  html, body {
    width: 1200px;
    height: 875px;
    overflow: hidden;
    background: var(--backdrop);
    font-family: "Montserrat", sans-serif;
  }
  .stage {
    width: 1200px;
    height: 875px;
    display: flex;
    align-items: center;
    justify-content: center;
    gap: 40px;
  }
  .card {
    width: 540px;
    height: 309px;
    flex: none;
    background: var(--card);
    border-radius: 22px;
    padding: 0 40px;
    display: flex;
    align-items: center;
    justify-content: center;
    overflow: hidden;
  }

  /* Logo lockup (shared) */
  .lockup {
    display: flex;
    flex-direction: column;
    align-items: flex-start;
    width: max-content;
    flex: none;
  }
  .brand-mark { display: flex; align-items: center; white-space: nowrap; }
  .brand-square { background: var(--brand-blue); flex: none; }
  .brand-text { display: flex; flex-direction: column; }
  .brand-name {
    font-weight: 800;
    color: var(--ink);
    text-transform: uppercase;
    line-height: 1;
  }
  .brand-sub {
    font-weight: 600;
    color: var(--ink);
    text-transform: uppercase;
    line-height: 1.1;
  }
  .brand-rule { align-self: stretch; background: var(--brand-blue); }
  .phone-display {
    font-family: "Black Ops One", sans-serif;
    color: var(--ink);
    white-space: nowrap;
    line-height: 1;
  }

  /* Front sizes */
  .front .brand-mark { gap: 14px; }
  .front .brand-square { width: 26px; height: 26px; }
  .front .brand-name { font-size: 44px; }
  .front .brand-sub { font-size: 15px; letter-spacing: 1.5px; margin-top: 4px; }
  .front .brand-rule { height: 3px; margin: 10px 0 12px; }
  .front .phone-display { font-size: 52px; letter-spacing: 1px; }

  /* Back sizes */
  .back { justify-content: flex-start; padding-left: 46px; }
  .back .brand-mark { gap: 7px; }
  .back .brand-square { width: 12px; height: 12px; }
  .back .brand-name { font-size: 20px; }
  .back .brand-sub { font-size: 7.5px; letter-spacing: 0.6px; margin-top: 2px; }
  .back .brand-rule { height: 2px; margin: 5px 0 6px; }
  .back .phone-display { font-size: 25px; }

  .divider { width: 1.5px; height: 110px; background: var(--brand-blue); margin: 0 18px; flex: none; }
  .contact { display: flex; flex-direction: column; gap: 8px; min-width: 0; }
  .contact-name { font-weight: 600; font-size: 21px; color: var(--brand-blue); white-space: nowrap; }
  .contact-email { display: flex; align-items: center; gap: 7px; font-size: 11px; color: var(--text-muted); white-space: nowrap; }
  .contact-email svg { flex: none; }
  .services { font-size: 11px; color: var(--text-muted); line-height: 1.35; max-width: 180px; }
</style>
</head>
<body>
<main class="stage">
  <section class="card front" aria-label="Business card front">
    <div class="lockup">
      <div class="brand-mark">
        <span class="brand-square"></span>
        <div class="brand-text">
          <span class="brand-name">Brindale</span>
          <span class="brand-sub">Transport Maintenance</span>
        </div>
      </div>
      <div class="brand-rule"></div>
      <div class="phone-display">0452819036</div>
    </div>
  </section>

  <section class="card back" aria-label="Business card back">
    <div class="lockup">
      <div class="brand-mark">
        <span class="brand-square"></span>
        <div class="brand-text">
          <span class="brand-name">Brindale</span>
          <span class="brand-sub">Transport Maintenance</span>
        </div>
      </div>
      <div class="brand-rule"></div>
      <div class="phone-display">0452819036</div>
    </div>
    <div class="divider"></div>
    <div class="contact">
      <div class="contact-name">Ronan Brindale</div>
      <div class="contact-email">
        <svg width="12" height="9" viewBox="0 0 12 9" aria-hidden="true">
          <rect x="0" y="0" width="12" height="9" rx="1" fill="var(--brand-blue)"/>
          <path d="M0.5 0.8 L6 5 L11.5 0.8" stroke="#fff" stroke-width="1.2" fill="none"/>
        </svg>
        <span>Brindaletm@fernmail.com</span>
      </div>
      <div class="services">Onsite Cars, Trucks &amp; trailer maintenance and repairs</div>
    </div>
  </section>
</main>
</body>
</html>
```